Rise Forward: Leave Behind Old Patterns, Quit Drifting Through Days, Begin Shaping each Morning

Good day! I am excited to work again with you, amazing designers! This time I am looking for the cover design of my book.
Dimensions 6” x 9”
The book name is as my name project. I love simplicity, but yet that is impactful. I love colours, I don't have a specific colour in mind, but I like the mustard colour as the one in the logo of my company. I am open to ideas! I have attached some cover samples that I like so that it gives a better idea of what I have on mind.
I am looking for something that looks professional, yet, not super serious, that it's approachable to people. Something that calls their attention at first glance.
I am working with my editor and my interior designer as well to finalize this part of the book. I will be working with the person that I select for the book design to finalize it.
About the book, here a passage of an unedited version of the introduction for guidance :
My intention is to take you on a journey to help you to understand what is going on in your mind so that you get out from anything that is holding you back in your life. My intention is to guide you to start fully living and experiencing a life that your mind even have yet conceived. To experience a life where you live fearless and without suffering. Living your life where you are the navigator and the creator of how you are experiencing it and you are living in a world of possibilities where there are no limitations.
For it, we will start to understand more about the mind and about the brain. I am not a neuroscientist and neither I consider my self an expert in the workings of the brain, what I know is the result of my fascination about our brain. This curiosity and the part of me that likes to understand how things work took me to read, research and learn about how our brain works and how its intrinsic mechanisms are subconsciously influencing and limiting us. I encourage you to stay on this part, it can be a bit technical, but understanding how it works will empower you not to allow your mind to dictate the way you approach your life and to live on autopilot.
We will continue to describe how you have been programmed throughout your life, putting you inside a box limited by your subconscious beliefs and ideas about the world. In this part, we will also discuss what ego is, how it is subconsciously limiting you and how the ways of when ego manifests itself are limiting you and making you suffer. Now that you know how you have been enclosed in your mind for all your life, we will move to discuss how you can get out of it. You will learn how to master your emotions to eliminate your suffering and not allow them to control the direction of your life and use them as a mechanism to get out from your programed mind. We continue to discuss how to leverage the power of your mind and harness your power of choice. Finally, I invite you to see yourself as a holistic being so that you start truly living and take control over the direction of your life, by nourishing and taking care of all those aspects of you utilizing their wisdom and synergy to achieve higher connection within yourself, your soul and live your life in a higher level of consciousness with peace, flow, love and purpose.

```html
<!DOCTYPE html>
<html lang="en">
<head>
<meta charset="utf-8">
<title>Rise Forward — Book Cover</title>
<link rel="stylesheet" href="https://fonts.googleapis.com/css2?family=Arvo:wght@400&family=Montserrat:wght@700;800&display=swap">
<style>
  :root {
    --mustard: #F3D84A;
    --mustard-deep: #D6BB34;
    --ink: #2E2226;
    --cream: #FDF7E4;
    --iris: #5BC0D6;
    --stage: #ECECEC;
    --white: #FFFFFF;
  }
  * { margin: 0; padding: 0; box-sizing: border-box; }
  html, body { width: 1200px; height: 1200px; overflow: hidden; }
  body { background: var(--stage); position: relative; }

  .cover {
    position: absolute;
    left: 219px; top: 30px;
    width: 762px; height: 1140px;
    background: var(--mustard);
    overflow: hidden;
  }
  .title-arch {
    position: absolute;
    left: 85px; top: 0;
    width: 607px; height: 530px;
    background: var(--ink);
    border-radius: 0 0 304px 304px;
  }
  .book-title {
    position: absolute;
    right: 139px; top: 118px;
    text-align: right;
    font-family: "Montserrat", sans-serif;
    font-weight: 800;
    font-size: 86px;
    line-height: 0.95;
    color: var(--mustard);
    letter-spacing: -1px;
  }
  .eye-art {
    position: absolute;
    left: 215px; top: 360px;
    width: 345px; height: 150px;
    border-radius: 12px;
    background: linear-gradient(180deg, var(--cream) 0%, #E6EDE0 100%);
  }
  .subtitle {
    position: absolute;
    left: 108px; top: 560px;
    width: 540px;
    text-align: center;
    font-family: "Arvo", serif;
    font-size: 36px;
    line-height: 50px;
    color: var(--white);
  }
  .shape { position: absolute; }
  .dot-cream {
    left: 418px; top: 743px; width: 26px; height: 26px;
    border-radius: 50%; background: var(--cream);
  }
  .ring-small {
    left: 356px; top: 806px; width: 30px; height: 30px;
    border-radius: 50%; border: 3px solid var(--ink);
  }
  .ring-large {
    left: 435px; top: 765px; width: 292px; height: 292px;
    border-radius: 50%; border: 4px solid var(--ink);
  }
  .search-icon { left: 52px; top: 625px; width: 80px; height: 110px; }
  .compass-art {
    position: absolute;
    left: 12px; top: 754px; width: 292px; height: 292px;
    border-radius: 50%;
    background: radial-gradient(circle at 50% 50%, var(--cream) 0%, var(--mustard-deep) 100%);
  }
  .author-plate {
    position: absolute;
    left: 138px; top: 927px;
    width: 485px; height: 119px;
    background: var(--ink);
    display: flex; align-items: center; justify-content: center;
    font-family: "Montserrat", sans-serif;
    font-weight: 700;
    font-size: 40px;
    color: var(--white);
    letter-spacing: 0.5px;
  }
</style>
</head>
<body>
  <main class="cover">
    <div class="title-arch"></div>
    <h1 class="book-title">RISE<br>FORWARD:</h1>
    <div class="eye-art" role="img" aria-label="Illustration area: a wide open eye with a blue iris and lashes"></div>

    <p class="subtitle">Leave Behind Old Patterns, Quit Drifting Through Days, Begin Shaping each Morning</p>

    <span class="shape dot-cream"></span>
    <span class="shape ring-small"></span>
    <span class="shape ring-large"></span>

    <svg class="shape search-icon" viewBox="0 0 80 110" aria-hidden="true">
      <circle cx="44" cy="34" r="26" fill="var(--mustard-deep)"/>
      <circle cx="40" cy="34" r="24" fill="none" stroke="var(--ink)" stroke-width="5"/>
      <line x1="28" y1="58" x2="14" y2="98" stroke="var(--ink)" stroke-width="7" stroke-linecap="round"/>
      <line x1="28" y1="58" x2="14" y2="98" stroke="var(--mustard)" stroke-width="2" stroke-linecap="round"/>
    </svg>

    <div class="compass-art" role="img" aria-label="Illustration area: a compass with a cream dial and pointer"></div>

    <div class="author-plate">LORENA CASTELL</div>
  </main>
</body>
</html>
```